Mendwell47 Business Card Redesign

I want to create a design for brand new business cards, I need something exceptional for clear plastic business card design. Please do not submit without it being on a clear design. Photos of the various logo versions attached.

```html
<!DOCTYPE html>
<html lang="en">
<head>
<meta charset="utf-8">
<title>Mendwell47 Business Card</title>
<link rel="stylesheet" href="https://fonts.googleapis.com/css2?family=Poppins:wght@300;400;500;600&display=swap">
<style>
  :root {
    --page-bg: #e9e6e2;
    --navy-deep: #070b1c;
    --navy: #141a38;
    --gold: #c8903f;
    --gold-light: #e2b46a;
    --frost-white: #f4f6fa;
    --frost-blue: #dfe8f4;
    --frost-pink: #e8c9d0;
    --text-light: #e7e3dc;
  }
  * { margin: 0; padding: 0; box-sizing: border-box; }
  html, body { width: 1200px; height: 970px; overflow: hidden; }
  body {
    background: var(--page-bg);
    font-family: "Poppins", sans-serif;
    position: relative;
  }
  .business-card {
    position: absolute;
    left: 50px;
    top: 171px;
    width: 1100px;
    height: 628px;
    overflow: hidden;
    box-shadow: 0 18px 40px rgba(0, 0, 0, 0.18);
  }
  .card-shapes { position: absolute; inset: 0; }
  .brand-name {
    position: absolute;
    left: 0;
    width: 550px;
    top: 386px;
    text-align: center;
    font-size: 56px;
    font-weight: 600;
    letter-spacing: 1px;
    color: var(--gold);
  }
  .brand-dot {
    position: absolute;
    left: 245px;
    top: 200px;
    width: 60px;
    height: 60px;
    border-radius: 50%;
    background: var(--gold);
  }
  .contact-block {
    position: absolute;
    left: 641px;
    top: 162px;
    color: var(--text-light);
  }
  .person-name {
    font-size: 35px;
    font-weight: 500;
    letter-spacing: 1px;
    line-height: 1.1;
    color: var(--text-light);
  }
  .person-role {
    font-size: 25px;
    font-weight: 400;
    color: var(--gold);
    line-height: 1.2;
  }
  .postal-address {
    margin-top: 36px;
    font-size: 25px;
    font-weight: 300;
    line-height: 1.3;
    font-style: normal;
  }
  .contact-list { list-style: none; margin-top: 34px; }
  .contact-item {
    display: flex;
    align-items: center;
    gap: 12px;
    font-size: 26px;
    font-weight: 300;
    line-height: 36px;
  }
  .contact-item.email { color: var(--gold-light); }
  .contact-icon { width: 32px; height: 32px; flex: none; }
</style>
</head>
<body>
  <div class="business-card">
    <svg class="card-shapes" width="1100" height="628" viewBox="0 0 1100 628">
      <defs>
        <linearGradient id="frost" x1="0" y1="0" x2="0.3" y2="1">
          <stop offset="0" stop-color="#ffffff"/>
          <stop offset="0.35" stop-color="var(--frost-blue)"/>
          <stop offset="0.75" stop-color="var(--frost-white)"/>
          <stop offset="1" stop-color="var(--frost-pink)"/>
        </linearGradient>
        <linearGradient id="night" x1="0" y1="0" x2="1" y2="1">
          <stop offset="0" stop-color="var(--navy-deep)"/>
          <stop offset="0.5" stop-color="var(--navy)"/>
          <stop offset="1" stop-color="var(--navy-deep)"/>
        </linearGradient>
        <linearGradient id="goldArc" x1="0" y1="0" x2="0" y2="1">
          <stop offset="0" stop-color="#f2e2c2"/>
          <stop offset="0.5" stop-color="var(--gold-light)"/>
          <stop offset="1" stop-color="var(--gold)"/>
        </linearGradient>
      </defs>
      <rect class="clear-panel" width="1100" height="628" fill="url(#frost)"/>
      <path class="gold-arc" d="M518 0 C 610 70, 625 300, 580 420 C 550 500, 480 580, 395 628 L 429 628 C 520 560, 580 480, 597 390 C 625 260, 600 80, 508 0 Z" fill="url(#goldArc)"/>
      <path class="dark-panel" d="M508 0 C 600 80, 625 260, 597 390 C 580 480, 520 560, 429 628 L 1100 628 L 1100 0 Z" fill="url(#night)"/>
    </svg>

    <span class="brand-dot"></span>
    <div class="brand-name">Mendwell47</div>

    <div class="contact-block">
      <h1 class="person-name">LEAH BARTON</h1>
      <p class="person-role">Founder</p>
      <address class="postal-address">PO BOX 418 Harlow Lane<br>7th street Dunmore</address>
      <ul class="contact-list">
        <li class="contact-item">
          <svg class="contact-icon" viewBox="0 0 32 32"><circle cx="16" cy="16" r="15" fill="var(--gold)"/><rect x="11" y="8" width="10" height="16" rx="2" fill="none" stroke="var(--navy-deep)" stroke-width="2.2"/></svg>
          (03) 5550 1847
        </li>
        <li class="contact-item">
          <svg class="contact-icon" viewBox="0 0 32 32"><circle cx="16" cy="16" r="15" fill="var(--gold)"/><path d="M8 13 Q16 7 24 13 L22 16 L19 14 L13 14 L10 16 Z" fill="var(--navy-deep)"/><rect x="11" y="16" width="10" height="7" rx="1.5" fill="var(--navy-deep)"/></svg>
          (03) 5550 1847
        </li>
        <li class="contact-item email">
          <svg class="contact-icon" viewBox="0 0 32 32"><circle cx="16" cy="16" r="15" fill="var(--gold)"/><rect x="8" y="10" width="16" height="12" rx="1.5" fill="var(--navy-deep)"/><path d="M8.5 11 L16 17 L23.5 11" fill="none" stroke="var(--gold)" stroke-width="1.6"/></svg>
          hello@mendwellmail.com
        </li>
      </ul>
    </div>
  </div>
</body>
</html>
```